Business Card & Stationary for Jeweller | ||
Pearl Marquise Inc. | ||
Use same font as used in my logo | ||
Modern Professional Bright & Fun-filled |
Lorraine Whitcombe | ||
President & Principal Designer | ||
By Appointment | ||
lwhitcombe@pearlmarquise-example.ca | ||
www.pearlmarquise-example.ca | ||
Please add: Chatterbook Logo plus www.chatterbook-example.com/PearlMarquiseGems Chirpline Logo plus @RovingGemsmith NCF (National Crystalline Foundation) Logo Ethical Gemcraft Alliance Logo **I would like to incorporate a white background with black polka dots somehow on both the business card and stationary. I want glamour, trendy, feminine.** |
We customize each design experience to the clients requirements and bring our expertise and design tools to you! Complimentary Diamond Insurance for 12 months after purchase. Lifetime Manufacturing Warranty Free Lifetime Trade-Up Program Complimentary Champagne Delivery by Appointment Included |

```html
<!DOCTYPE html>
<html lang="en">
<head>
<meta charset="utf-8">
<title>Pearl Marquise Inc. — Business Card</title>
<link rel="stylesheet" href="https://fonts.googleapis.com/css2?family=Cormorant+Garamond:wght@500;600&family=Lato:wght@400;700&display=swap">
<style>
  :root {
    --stage: #ecebea;
    --card-white: #ffffff;
    --pink: #f0709f;
    --pink-soft: #f9c6d9;
    --pink-pale: #fde7ef;
    --ink: #6d6d6d;
    --rule: #e3a7bd;
    --on-pink: #ffffff;
    --dot: #1a1a1a;
  }
  * { box-sizing: border-box; margin: 0; padding: 0; }
  html, body { width: 1200px; height: 629px; overflow: hidden; }
  body {
    background: var(--stage);
    font-family: "Lato", sans-serif;
    display: flex;
    align-items: center;
    justify-content: center;
    gap: 40px;
  }
  .card {
    width: 540px;
    height: 309px;
    box-shadow: 0 6px 18px rgba(0,0,0,.15);
    position: relative;
    overflow: hidden;
  }

  /* Front */
  .card-front {
    background: var(--card-white);
    display: flex;
    align-items: center;
  }
  .polka-band {
    position: absolute;
    left: 0;
    right: 0;
    bottom: 0;
    height: 18px;
    background-color: var(--card-white);
    background-image: radial-gradient(circle, var(--dot) 2.2px, transparent 2.6px);
    background-size: 12px 12px;
    background-position: 0 3px;
  }
  .brand-block {
    width: 220px;
    height: 100%;
    display: flex;
    flex-direction: column;
    align-items: center;
    justify-content: center;
    gap: 12px;
  }
  .crest-ornament {
    width: 140px;
    height: 122px;
    border-radius: 50%;
    background: radial-gradient(circle, var(--pink-pale) 0%, var(--pink-soft) 70%, rgba(249,198,217,0) 100%);
  }
  .brand-name {
    font-family: "Cormorant Garamond", serif;
    font-weight: 600;
    font-size: 22px;
    color: var(--pink);
  }
  .divider {
    width: 1px;
    height: 190px;
    background: var(--rule);
  }
  .contact-block {
    padding: 0 18px 0 20px;
    flex: 1;
    min-width: 0;
  }
  .person-name {
    font-family: "Cormorant Garamond", serif;
    font-weight: 600;
    font-size: 20px;
    color: var(--pink);
  }
  .person-title {
    font-size: 10px;
    color: var(--ink);
    margin: 2px 0 14px;
  }
  .contact-list { list-style: none; }
  .contact-list li {
    display: flex;
    align-items: flex-start;
    gap: 7px;
    font-size: 9.5px;
    line-height: 12px;
    color: var(--ink);
    margin-bottom: 6px;
  }
  .contact-text { min-width: 0; overflow-wrap: anywhere; }
  .contact-text .network { display: block; }
  .contact-icon { width: 12px; height: 12px; flex: none; }

  /* Back */
  .card-back {
    background: var(--pink);
    padding: 120px 34px 0 34px;
  }
  .promise-list { list-style: none; }
  .promise-list li {
    color: var(--on-pink);
    font-size: 11px;
    line-height: 1.35;
    margin-bottom: 8px;
    max-width: 400px;
  }
</style>
</head>
<body>
  <section class="card card-front">
    <div class="brand-block">
      <div class="crest-ornament" role="img" aria-label="Pink crown and gem crest ornament with flourishes"></div>
      <div class="brand-name">Pearl Marquise</div>
    </div>
    <div class="divider"></div>
    <div class="contact-block">
      <div class="person-name">Lorraine Whitcombe</div>
      <div class="person-title">President &amp; Principal Designer</div>
      <ul class="contact-list">
        <li>
          <svg class="contact-icon" viewBox="0 0 12 12"><circle cx="6" cy="6" r="6" fill="var(--pink)"/><path d="M4 3.2l1 1.3-.6.7a4 4 0 0 0 2.4 2.4l.7-.6 1.3 1-.5.9c-2.6 0-4.8-2.2-4.8-4.8z" fill="#fff"/></svg>
          <span class="contact-text">1 (555) 014-2290</span>
        </li>
        <li>
          <svg class="contact-icon" viewBox="0 0 12 12"><circle cx="6" cy="6" r="6" fill="var(--pink)"/><path d="M4 3.2l1 1.3-.6.7a4 4 0 0 0 2.4 2.4l.7-.6 1.3 1-.5.9c-2.6 0-4.8-2.2-4.8-4.8z" fill="#fff"/></svg>
          <span class="contact-text">1 (555) 014-2291</span>
        </li>
        <li>
          <svg class="contact-icon" viewBox="0 0 12 12"><circle cx="6" cy="6" r="6" fill="var(--pink)"/><rect x="3" y="4" width="6" height="4" fill="none" stroke="#fff" stroke-width=".8"/><path d="M3 4l3 2.2L9 4" fill="none" stroke="#fff" stroke-width=".8"/></svg>
          <span class="contact-text">lwhitcombe@pearlmarquise-example.ca</span>
        </li>
        <li>
          <svg class="contact-icon" viewBox="0 0 12 12"><circle cx="6" cy="6" r="6" fill="var(--pink)"/><circle cx="6" cy="6" r="3" fill="none" stroke="#fff" stroke-width=".8"/><path d="M3 6h6M6 3v6" stroke="#fff" stroke-width=".6"/></svg>
          <span class="contact-text">www.pearlmarquise-example.ca</span>
        </li>
        <li>
          <svg class="contact-icon" viewBox="0 0 12 12"><circle cx="6" cy="6" r="6" fill="var(--pink)"/></svg>
          <span class="contact-text"><span class="network">Chatterbook</span>www.chatterbook-example.com/PearlMarquiseGems</span>
        </li>
        <li>
          <svg class="contact-icon" viewBox="0 0 12 12"><circle cx="6" cy="6" r="6" fill="var(--pink)"/></svg>
          <span class="contact-text">Chirpline · @RovingGemsmith</span>
        </li>
      </ul>
    </div>
    <div class="polka-band"></div>
  </section>

  <section class="card card-back">
    <ul class="promise-list">
      <li>We customize each design experience to the clients requirements and bring our expertise and design tools to you!</li>
      <li>Complimentary Diamond Insurance for 12 months after purchase.</li>
      <li>Lifetime Manufacturing Warranty</li>
      <li>Free Lifetime Trade-Up Program</li>
      <li>Complimentary Champagne Delivery by Appointment Included</li>
    </ul>
  </section>
</body>
</html>
```